business card for author of crime novel

I am an author with a new book. I need a business card with the book's cover on one side (already uploaded), and contact details on the other.

Walt Pemberty
Author

telephone: 646-512-7380
website: www.waltpemberty.net
facebook: friendwall.com/wpemberty
twitter: chirpnote.com/wpemberty
email: wpemberty@postvale.net

Target Market(s)

Readers of mystery books

Industry/Entity Type

Business

Contact Information for Business Card

Walt Pemberty
Author

telephone: 646-512-7380

Font styles to use
Serif
Sans Serif

Requirements
Must have
• Book cover on one side. My contact info on the other, with the name of the book repeated if that makes sense. Clean design.
Should not have
• Overly ornate, too formal, too distracting

```html
<!DOCTYPE html>
<html lang="en">
<head>
<meta charset="utf-8">
<title>Walt Pemberty – Business Card</title>
<link rel="stylesheet" href="https://fonts.googleapis.com/css2?family=Marcellus&family=Crimson+Pro:ital,wght@0,400;0,700;1,400&display=swap">
<style>
  :root {
    --backdrop: #8d9fa9;
    --card: #b8862a;
    --ink: #1a1510;
    --paper-text: #f3ecd9;
    --frame: #5d7880;
    --author-yellow: #e8e21a;
    --label-paper: #e2cfa6;
    --photo-dark: #2f4650;
    --photo-light: #8fa7ae;
  }
  * { margin: 0; padding: 0; box-sizing: border-box; }
  html, body { width: 1200px; height: 720px; overflow: hidden; }
  body { background: var(--backdrop); position: relative; font-family: "Crimson Pro", serif; }

  .card {
    position: absolute;
    width: 300px;
    height: 524px;
    background: var(--card);
  }
  .card--cover { left: 264px; top: 100px; }
  .card--contact { left: 638px; top: 98px; }

  /* Cover side */
  .cover-title {
    position: absolute;
    top: 30px; left: 0; width: 100%;
    text-align: center;
    font-family: "Crimson Pro", serif;
    font-weight: 700;
    font-size: 29px;
    line-height: 1;
    color: var(--ink);
    letter-spacing: 2px;
  }
  .cover-photo {
    position: absolute;
    left: 14px; top: 78px;
    width: 271px; height: 364px;
    display: block;
  }
  .cover-author {
    position: absolute;
    left: 118px; width: 180px; top: 388px;
    text-align: center;
    font-family: "Marcellus", serif;
    font-size: 19px;
    line-height: 23px;
    color: var(--author-yellow);
    letter-spacing: 0.5px;
  }
  .series-label {
    position: absolute;
    left: 14px; top: 458px;
    width: 270px; height: 40px;
    background: var(--label-paper);
    border-radius: 3px;
    display: flex; align-items: center; justify-content: center;
    font-family: "Crimson Pro", serif;
    font-size: 20px;
    color: var(--ink);
  }

  /* Contact side */
  .contact-frame {
    position: absolute;
    left: 15px; top: 80px;
    width: 272px; height: 364px;
    border: 1px solid var(--frame);
  }
  .contact-text {
    position: absolute;
    color: var(--paper-text);
    font-size: 18px;
    line-height: 1;
    white-space: nowrap;
  }
  .name-first, .name-last, .role {
    position: absolute;
    color: var(--ink);
    font-weight: 700;
    line-height: 1;
    white-space: nowrap;
  }
  .name-first { left: 196px; top: 38px; font-size: 26px; }
  .name-last { left: 256px; top: 62px; font-size: 26px; writing-mode: vertical-rl; }
  .role { left: 24px; bottom: 61px; font-size: 22px; }
  .rise { writing-mode: vertical-rl; transform: rotate(180deg); }

  .phone { left: 44px; top: 44px; font-size: 19px; }
  .phone .phone-mark { font-style: italic; }
  .website { left: 30px; bottom: 183px; }
  .email { left: 60px; bottom: 186px; }
  .chirp-domain { left: 135px; top: 426px; }
  .chirp-handle { left: 231px; bottom: 86px; }
  .wall-domain { left: 150px; top: 455px; }
  .wall-handle { left: 262px; bottom: 61px; }
</style>
</head>
<body>
  <section class="card card--cover" aria-label="Book cover side">
    <h1 class="cover-title">THE NIGHT DESK</h1>
    <svg class="cover-photo" viewBox="0 0 271 364" role="img" aria-label="Photograph of an old tenement building with fire escapes, in blue-grey tones">
      <defs>
        <linearGradient id="photoTone" x1="0" y1="0" x2="1" y2="1">
          <stop offset="0" stop-color="var(--photo-light)"/>
          <stop offset="1" stop-color="var(--photo-dark)"/>
        </linearGradient>
      </defs>
      <rect width="271" height="364" fill="url(#photoTone)"/>
    </svg>
    <p class="cover-author">WALT<br>PEMBERTY</p>
    <p class="series-label">A Harlan Booth Mystery</p>
  </section>

  <section class="card card--contact" aria-label="Contact side">
    <div class="contact-frame"></div>
    <p class="contact-text phone"><span class="phone-mark">T</span> 646-512-7380</p>
    <p class="name-first">Walt</p>
    <p class="name-last">Pemberty</p>
    <p class="contact-text website rise">www.waltpemberty.net</p>
    <p class="contact-text email rise">wpemberty@postvale.net</p>
    <p class="role rise">Author</p>
    <p class="contact-text chirp-domain">chirpnote.com</p>
    <p class="contact-text chirp-handle rise">/wpemberty</p>
    <p class="contact-text wall-domain">friendwall.com</p>
    <p class="contact-text wall-handle rise">/wpemberty</p>
  </section>
</body>
</html>
```